Graphics for Corvella telehealth weight loss plans

Corvella focuses on delivering medical weight-loss using prescription medicine and telehealth consults. Corvella needs graphics for its ecommerce site for three weight loss plans. The plans are posted here with current graphics and descriptions of what is included with each plan. Please do not feel constrained by current graphics or styling.

- https://store.corvellacare.com/products/radiant-horizon-plan
- https://store.corvellacare.com/products/brightpath-core-plan
- https://store.corvellacare.com/products/daily-harbor-plan

The graphics need to look good on mobile and desktop browsers.

```html
<!DOCTYPE html>
<html lang="en">
<head>
<meta charset="utf-8">
<title>Corvella plan graphics</title>
<link rel="stylesheet" href="https://fonts.googleapis.com/css2?family=Fira+Sans:wght@400;500;600;700&family=Fira+Sans+Condensed:wght@600;700&family=PT+Sans&display=swap">
<style>
  :root {
    --page-bg: #e3ecf6;
    --ink: #1d1d22;
    --ink-soft: #2b2b30;
    --power-bg-top: #d6dcea;
    --power-bg-bottom: #aab5c8;
    --power-price: #fdf16a;
    --transform-bg-left: #c9c9cb;
    --transform-bg-right: #ffffff;
    --transform-price: #f7709c;
    --renewal-bg: #c3c4c7;
    --renewal-price-ink: #0d2f66;
    --white: #ffffff;
    --frame-line: #9a9ca2;
  }
  * { box-sizing: border-box; margin: 0; padding: 0; }
  html, body { width: 1200px; height: 640px; overflow: hidden; }
  body {
    position: relative;
    background: var(--page-bg);
    font-family: "Fira Sans", sans-serif;
    color: var(--ink);
  }
  .presentation-note {
    position: absolute; left: 0; top: 58px; width: 1200px;
    text-align: center;
    font-family: "PT Sans", sans-serif;
    font-size: 29px; color: #111;
  }
  .plan-card {
    position: absolute; top: 135px; width: 317px; height: 449px;
    overflow: hidden;
  }
  .brand {
    position: absolute;
    display: flex; align-items: center; gap: 4px;
    font-family: "Fira Sans", sans-serif; font-weight: 500;
    font-size: 11px; color: var(--ink-soft); letter-spacing: 0.5px;
  }
  .brand-square { width: 7px; height: 7px; border: 1.2px solid var(--ink-soft); }
  .media { position: absolute; }
  .price {
    position: absolute; display: flex; align-items: center; justify-content: center;
    font-family: "Fira Sans Condensed", sans-serif; font-weight: 700;
  }

  /* Card 1 */
  .card-power {
    left: 108px;
    background: linear-gradient(180deg, var(--power-bg-top) 0%, #bcc5d6 45%, var(--power-bg-bottom) 100%);
  }
  .card-power .brand { left: 19px; top: 24px; }
  .card-power .hero-art {
    left: 45px; top: 37px; width: 233px; height: 135px; border-radius: 6px;
    background: radial-gradient(ellipse at 50% 45%, #e9eaee 0%, #d8d3a4 40%, #c9cfdc 80%);
  }
  .card-power .faded-portrait {
    left: 150px; top: 200px; width: 167px; height: 249px;
    background: radial-gradient(ellipse at 50% 40%, rgba(210,190,180,0.35), rgba(170,181,200,0) 70%);
  }
  .card-power .plan-title {
    position: absolute; left: 0; width: 100%; top: 193px; text-align: center;
    font-family: "Fira Sans Condensed", sans-serif; font-weight: 700;
    font-size: 20px; color: #2a2a30;
  }
  .card-power .price {
    left: 125px; top: 223px; width: 67px; height: 27px;
    background: var(--power-price); border-radius: 3px; font-size: 15px; color: #1a1a1a;
  }
  .card-power .includes {
    position: absolute; left: 11px; top: 262px; width: 294px; height: 172px;
    border: 1px solid rgba(120,130,150,0.55); border-radius: 12px;
    padding: 12px 0 0 14px;
  }
  .card-power .includes h3 { font-weight: 500; font-size: 14px; margin-bottom: 6px; }
  .card-power .includes li {
    list-style: none; font-size: 10.3px; line-height: 18.8px; color: #222; white-space: nowrap;
  }
  .card-power .includes strong { font-weight: 700; }

  /* Card 2 */
  .card-transform {
    left: 441px;
    background: linear-gradient(90deg, var(--transform-bg-left) 0%, #ececec 55%, var(--transform-bg-right) 100%);
  }
  .card-transform .brand { left: 134px; top: 28px; font-size: 13px; }
  .card-transform .portrait {
    left: 229px; top: 23px; width: 84px; height: 426px; border-radius: 40px 40px 20px 20px;
    background: linear-gradient(180deg, #e4c3ae 0%, #f17aa3 30%, #e7c6b2 45%, #b9babd 60%, #cfd0d2 100%);
    opacity: 0.8;
  }
  .card-transform .plan-title {
    position: absolute; left: 21px; top: 72px;
    font-family: "Fira Sans Condensed", sans-serif; font-weight: 700;
    font-size: 25px; line-height: 24px; color: #38383c;
  }
  .card-transform .price {
    left: 78px; top: 153px; width: 89px; height: 35px;
    background: var(--transform-price); color: var(--white); font-size: 19px; border-radius: 2px;
  }
  .card-transform .includes-heading {
    position: absolute; left: 15px; top: 211px; width: 207px;
    display: flex; align-items: center; gap: 5px;
    font-family: "Fira Sans Condensed", sans-serif; font-weight: 600; font-size: 16px; color: #2a2a2e;
  }
  .card-transform .includes-heading::after {
    content: ""; flex: 1; height: 1.4px; background: #2a2a2e;
  }
  .card-transform .includes-list {
    position: absolute; left: 15px; top: 242px; width: 210px;
    padding-left: 12px; font-family: "Fira Sans Condensed", sans-serif; font-weight: 600;
    font-size: 11.2px; line-height: 15.4px; color: #2a2a2e;
  }
  .card-transform .includes-list li { white-space: nowrap; }

  /* Card 3 */
  .card-renewal {
    left: 775px;
    background: radial-gradient(ellipse at 50% 70%, #d0d1d4 0%, var(--renewal-bg) 70%, #b8b9bc 100%);
  }
  .card-renewal .brand { left: 16px; top: 20px; font-size: 10px; }
  .card-renewal .frame-line {
    position: absolute; border: 1px solid var(--frame-line);
  }
  .card-renewal .photo { position: absolute; }
  .card-renewal .photo-main {
    left: 100px; top: 39px; width: 116px; height: 158px;
    background: linear-gradient(180deg, #dde4ee 0%, #c9a98a 35%, #6f7f98 70%, #5f6f8a 100%);
  }
  .card-renewal .photo-salad { left: 52px; top: 55px; width: 43px; height: 60px; background: linear-gradient(160deg, #3c4654, #5f8a46 60%, #2f3540); }
  .card-renewal .photo-doctor { left: 25px; top: 118px; width: 71px; height: 60px; background: linear-gradient(180deg, #e2e2e2, #f2f2f2 55%, #cfd3d8); }
  .card-renewal .photo-mealbox { left: 221px; top: 55px; width: 71px; height: 60px; background: linear-gradient(150deg, #2d2b36, #7a9a55 50%, #39353f); }
  .card-renewal .photo-waist { left: 221px; top: 118px; width: 43px; height: 60px; background: linear-gradient(180deg, #f2b7bb, #f4cfc6 55%, #e99fa8); }
  .card-renewal .plan-title {
    position: absolute; left: 0; width: 100%; top: 212px; text-align: center;
    font-family: "Fira Sans Condensed", sans-serif; font-weight: 600;
    font-size: 23px; color: #333338;
  }
  .card-renewal .price {
    left: 114px; top: 249px; width: 88px; height: 34px;
    background: var(--white); color: var(--renewal-price-ink); font-size: 18px;
  }
  .card-renewal .includes-heading {
    position: absolute; left: 108px; top: 300px; width: 101px; height: 23px;
    border: 1px solid #3a3a3e; display: flex; align-items: center; justify-content: center;
    font-family: "Fira Sans Condensed", sans-serif; font-weight: 600; font-size: 13px; color: #222;
  }
  .card-renewal .includes-list {
    position: absolute; left: 0; width: 100%; top: 335px; text-align: center;
    font-size: 10.2px; line-height: 18.5px; color: #1f1f22;
  }
  .card-renewal .includes-list li { list-style: none; }
</style>
</head>
<body>
  <p class="presentation-note">Here are 3 templated for 3 plans. Thanks!</p>

  <section class="plan-card card-power">
    <div class="media faded-portrait" role="img" aria-label="Faded photo of a smiling woman holding an apple"></div>
    <div class="brand"><span class="brand-square"></span>Corvella</div>
    <div class="media hero-art" role="img" aria-label="3D lose weight lettering wrapped in a yellow measuring tape with fruit"></div>
    <h2 class="plan-title">BRIGHTPATH CORE PLAN</h2>
    <div class="price">$199.00</div>
    <div class="includes">
      <h3>Plan includes</h3>
      <ul>
        <li>100% online. No need to visit the office</li>
        <li>Real Phentermine (37.5mg / pill) delivered to your door</li>
        <li>Phentermine prescription</li>
        <li>1 month supply (30 pills)</li>
        <li>Medical consultation</li>
        <li><strong>FREE</strong> Introductory Nutritionist consult on your first month</li>
        <li>Month-to-month pay as you go</li>
      </ul>
    </div>
  </section>

  <section class="plan-card card-transform">
    <div class="brand"><span class="brand-square"></span>Corvella</div>
    <div class="media portrait" role="img" aria-label="Photo of a fit woman in a pink sports top and grey sweatpants pointing forward"></div>
    <h2 class="plan-title">Radiant<br>Horizon<br>Plan</h2>
    <div class="price">$199.00</div>
    <h3 class="includes-heading">Plan includes</h3>
    <ol class="includes-list">
      <li>100% online. No need to visit the office.</li>
      <li>Real Phentermine (37.5mg / pill)<br>delivered to your door</li>
      <li>Phentermine prescription</li>
      <li>1 month supply (30 pills)</li>
      <li>Medical consultation</li>
      <li>Expert nutrition consult</li>
      <li>Custom crafted diet plan to achieve<br>your goals</li>
      <li>Nutrition coaching to improve your<br>health and vitality</li>
      <li>Month-to-month pay as you go</li>
    </ol>
  </section>

  <section class="plan-card card-renewal">
    <div class="brand"><span class="brand-square"></span>Corvella</div>
    <div class="frame-line" style="left:35px;top:78px;width:65px;height:112px;"></div>
    <div class="frame-line" style="left:216px;top:144px;width:60px;height:46px;"></div>
    <div class="frame-line" style="left:184px;top:30px;width:46px;height:24px;border-bottom:none;border-left:none;"></div>
    <div class="photo photo-salad" role="img" aria-label="Photo of hands holding a bowl of salad"></div>
    <div class="photo photo-doctor" role="img" aria-label="Photo of a doctor in a white coat"></div>
    <div class="photo photo-main" role="img" aria-label="Photo of a young woman holding a green apple with a measuring tape"></div>
    <div class="photo photo-mealbox" role="img" aria-label="Photo of healthy meal prep containers"></div>
    <div class="photo photo-waist" role="img" aria-label="Photo of a woman measuring her waist"></div>
    <h2 class="plan-title">Daily Harbor Plan</h2>
    <div class="price">$99.00</div>
    <h3 class="includes-heading">Plan includes</h3>
    <ul class="includes-list">
      <li>100% online. No need to visit the office.</li>
      <li>Expert nutrition consult</li>
      <li>Custom crafted diet plan to achieve your goals</li>
      <li>Nutrition coaching to improve your health and vitality</li>
      <li>Month-to-month pay as you go</li>
    </ul>
  </section>
</body>
</html>
```